BrightVale business cards

We want to create two sets of cards. One general card for brightvale [staff] and one card for the founder of the company. Below is the general/basic information for you to format/display on side of the cards:
--Company address: 418 Marlow Street, New York, NY 10034
--Main phone: 212-563-7182
Will also provide you with secondary 1-800 number
--company website: www.brightvale-example.com
--email address for general card: concierge@brightvale-example.com
--email address (for dr lindqvist's card: dr@brightvale-example.com
--titles for dr lindqvist's card: Founder, Medical Director
--Dr. Lindqvist's name on the card should read: Martin E. Lindqvist, MD
You can also play around with brightvale's tag line: Glow Starts With Care (TM or R should be attached as a trademark has been filed)
Reason: More time to design something awesome. This company is an aesthetic medical company that offers cool and safe cosmetic treatments
For the business card design for the doctor, please change the doctor's name to look like this above his title: Martin E. Lindqvist, MD instead of using Dr. Martin....etc
Reason: WILL NOT BE ABLE TO VIEW AND FINALIZE DESIGNS UNTIL I RETURN FROM MEDICAL CONFERENCE, WHICH WILL BE ON SUNDAY/MONDAY. MY APOLOGIES
can everyone try making it very minimalistic
A Bit of a change...
Can everyone take a stab at using a grey "raw" or eco friendly stock paper. We are interested to see the designs you come up with.
Business

```html
<!DOCTYPE html>
<html lang="en">
<head>
<meta charset="utf-8">
<title>BrightVale Business Cards</title>
<link href="https://fonts.googleapis.com/css2?family=Roboto+Condensed:wght@300;400;700&display=swap" rel="stylesheet">
<style>
  :root {
    --frame: #58585a;
    --sheet: #ffffff;
    --card-edge: #8a8a8a;
    --brand-blue: #3286c7;
    --logo-blue: #3b8fd6;
    --text-grey: #555555;
    --white: #ffffff;
  }
  * { margin: 0; padding: 0; box-sizing: border-box; }
  html, body { width: 1200px; height: 1200px; overflow: hidden; }
  body {
    background: var(--frame);
    font-family: "Roboto Condensed", "Arial Narrow", sans-serif;
    position: relative;
  }
  .sheet {
    position: absolute; left: 15px; top: 15px;
    width: 1170px; height: 1170px;
    background: var(--sheet);
  }
  .card {
    position: absolute; width: 494px; height: 282px;
    background: var(--white);
    border: 1px solid var(--card-edge);
  }
  .card--front-basic { left: 61px; top: 274px; }
  .card--front-concierge { left: 615px; top: 274px; }
  .card--founder { left: 61px; top: 616px; }
  .card--back { left: 615px; top: 616px; }

  .card__panel {
    position: absolute; left: 20px; top: 19px;
    width: 452px; height: 243px;
    background: var(--brand-blue);
  }
  .wordmark {
    position: absolute;
    font-weight: 400;
    line-height: 1;
    letter-spacing: -0.5px;
  }
  .wordmark__name { display: block; }
  .wordmark__tag {
    display: block;
    font-weight: 400;
    text-transform: uppercase;
  }
  .wordmark--light { color: var(--white); }
  .wordmark--blue { color: var(--logo-blue); }

  .divider {
    position: absolute; width: 0;
    border-left: 1px dotted rgba(255,255,255,0.75);
  }
  .divider--grey { border-left-color: #8c8c8c; }

  .contact {
    position: absolute;
    color: var(--white);
    font-weight: 300;
    font-size: 14.5px;
    line-height: 18px;
  }
  .contact p + p { margin-top: 0; }
  .contact .gap { margin-top: 10px; }

  .founder {
    position: absolute; left: 297px; top: 98px;
  }
  .founder__name {
    color: var(--logo-blue);
    font-weight: 400;
    font-size: 20px;
    line-height: 24px;
  }
  .founder__title {
    color: var(--text-grey);
    font-weight: 300;
    font-size: 13.5px;
    text-transform: uppercase;
    margin-top: 2px;
  }
  .founder__email {
    color: var(--text-grey);
    font-weight: 300;
    font-size: 17px;
    margin-top: 14px;
  }
</style>
</head>
<body>
<div class="sheet">

  <!-- Front: basic staff card -->
  <div class="card card--front-basic">
    <div class="card__panel">
      <div class="wordmark wordmark--light" style="left:40px; top:100px;">
        <span class="wordmark__name" style="font-size:36px;">brightvale</span>
        <span class="wordmark__tag" style="font-size:5px; letter-spacing:1.3px; margin-top:3px;">Glow Starts With Care™</span>
      </div>
      <div class="divider" style="left:239px; top:54px; height:132px;"></div>
      <div class="contact" style="left:284px; top:69px;">
        <p>418 Marlow Street</p>
        <p>New York, NY 10034</p>
        <p class="gap">212.563.7182</p>
        <p>1.800.000.0000</p>
        <p class="gap">www.brightvale-example.com</p>
      </div>
    </div>
  </div>

  <!-- Front: concierge card -->
  <div class="card card--front-concierge">
    <div class="card__panel">
      <div class="wordmark wordmark--light" style="left:40px; top:95px;">
        <span class="wordmark__name" style="font-size:36px;">brightvale</span>
        <span class="wordmark__tag" style="font-size:5px; letter-spacing:1.3px; margin-top:3px;">Glow Starts With Care™</span>
      </div>
      <div class="divider" style="left:240px; top:54px; height:144px;"></div>
      <div class="contact" style="left:280px; top:59px;">
        <p>418 Marlow Street</p>
        <p>New York, NY 10034</p>
        <p class="gap">212.563.7182</p>
        <p>1.800.000.0000</p>
        <p class="gap">www.brightvale-example.com</p>
        <p>concierge@brightvale-example.com</p>
      </div>
    </div>
  </div>

  <!-- Founder card -->
  <div class="card card--founder">
    <div class="wordmark wordmark--blue" style="left:22px; top:98px;">
      <span class="wordmark__name" style="font-size:52px;">brightvale</span>
      <span class="wordmark__tag" style="font-size:7px; letter-spacing:2px; margin-top:4px;">Glow Starts With Care™</span>
    </div>
    <div class="divider divider--grey" style="left:275px; top:78px; height:116px;"></div>
    <div class="founder">
      <p class="founder__name">Dr. Martin E. Lindqvist</p>
      <p class="founder__title">Founder, Medical Director</p>
      <p class="founder__email">dr@brightvale-example.com</p>
    </div>
  </div>

  <!-- Back: brand card -->
  <div class="card card--back">
    <div class="wordmark wordmark--blue" style="left:60px; top:84px;">
      <span class="wordmark__name" style="font-size:86px;">brightvale</span>
      <span class="wordmark__tag" style="font-size:12px; letter-spacing:3.4px; margin-top:6px;">Glow Starts With Care™</span>
    </div>
  </div>

</div>
</body>
</html>
```